Brisk Fixers 24 Postcard Design, Double-Sided

Please read carefully and see attached. Designers that do not follow these instructions will not be selected. Limit ONE design submission per artist. The ONE design submission shall show both the front and the back designs. Designs must comply with the attached dismensions accounting for the bleed area to prevent designs from being cut off during printing. The attached business card and door tag designs have already been created, printed and are in use. The postcard shall be similar in design to the attached business card and door tag. All of the information that you need is attached. The overall size is 4.12" x 6.12" for the front. The back is different, see attached and scale to match template. I would like the Veteran Owned Business logo added as well. It would also be nice to see my photo incorporated somehow. I like the yellow on the door tag. It helps build contrast and pops out. Again, one design submission per designer that shows both the front and the back.

Target Market(s)

Please read all instructions and see attached.

Industry/Entity Type

Requirements
Must have
• Please read all instructions and see attached.
Nice to have
Should not have

```html
<!DOCTYPE html>
<html lang="en">
<head>
<meta charset="utf-8">
<title>Brisk Fixers 24 Postcard</title>
<link href="https://fonts.googleapis.com/css2?family=Lato:ital,wght@0,400;0,700;0,900;1,700&family=Montserrat:wght@700;800;900&family=Dancing+Script:wght@600&display=swap" rel="stylesheet">
<style>
:root{
  --backdrop:#585858;
  --ink:#171c24;
  --yellow:#fde400;
  --white:#ffffff;
  --red:#e3262b;
  --grey-line:#9a9a9a;
}
*{box-sizing:border-box;margin:0;padding:0}
html,body{width:1200px;height:1200px;overflow:hidden}
body{background:var(--backdrop);font-family:'Lato',sans-serif;position:relative}
.card{position:absolute;left:214px;width:775px;height:523px;overflow:hidden;background:var(--white)}
.card-front{top:55px;background:var(--ink)}
.card-back{top:633px}
.abs{position:absolute}

/* front */
.photo-row{position:absolute;left:0;width:775px;height:116px;display:flex}
.photo-row.top{top:0}
.photo-row.bottom{top:408px;height:115px}
.photo{flex:1;height:100%;border-right:2px solid var(--white)}
.photo:last-child{border-right:0}
.ph-assembly{background:linear-gradient(135deg,#d9d3c8,#b9a98f)}
.ph-router{background:radial-gradient(circle at 50% 55%,#2fa6e8,#0b2a5a 70%)}
.ph-plumbing{background:linear-gradient(135deg,#f1f1f1,#c8c3bd)}
.ph-siding{background:linear-gradient(180deg,#cfd4d8,#a9b0b6)}
.ph-doorbell{background:linear-gradient(90deg,#8c8276 0 45%,#e4e4e4 45%)}
.ph-tvmount{background:linear-gradient(135deg,#f3d23b,#3a3a3a)}
.ph-curtain{background:linear-gradient(90deg,#f4f4f4,#6c6f78 50%,#e9e9e9)}
.ph-paint{background:linear-gradient(120deg,#9fc6dc,#d86ab6 45%,#8ccbe6)}

.front-topline{left:0;top:116px;width:775px;height:5px;background:var(--yellow)}
.front-bottomline{left:0;top:403px;width:430px;height:5px;background:var(--yellow)}
.front-tagstrip{left:0;top:124px;width:380px;height:60px;background:var(--yellow);border-radius:0 60px 0 0}
.tagline{left:31px;top:139px;font:900 16.5px/19px 'Lato',sans-serif;color:var(--ink)}
.services-pill{left:69px;top:200px;width:135px;height:29px;border:2px solid var(--yellow);border-radius:15px;color:var(--white);font:900 19px/25px 'Lato',sans-serif;text-align:center}
.services-list{left:47px;top:240px;list-style:none;color:var(--white);font:400 19.5px/21px 'Lato',sans-serif}
.services-list li::before{content:"";display:inline-block;width:7px;height:7px;background:var(--yellow);margin-right:8px;vertical-align:3px}

.brand-seal{left:263px;top:159px;width:208px;height:208px;border-radius:50%;background:var(--yellow);border:6px solid var(--ink);box-shadow:0 0 0 5px var(--yellow);display:flex;align-items:center;justify-content:center;text-align:center}
.brand-seal span{font:900 27px/30px 'Montserrat',sans-serif;color:var(--ink)}

.headline{left:502px;top:140px;font:700 29px/34px 'Lato',sans-serif;color:var(--white);white-space:nowrap}
.headline em{font-style:normal;font-weight:900;color:var(--yellow)}
.headline-rule{left:502px;top:178px;width:258px;height:2px;background:var(--white)}
.benefits{left:512px;top:203px;list-style:none;color:var(--white);font:400 18px/19.6px 'Lato',sans-serif}
.benefits li::before{content:"\2713";color:var(--yellow);font-weight:900;margin-right:8px}
.signature{font-family:'Dancing Script',cursive;color:var(--white);white-space:nowrap}
.front-signature{left:545px;top:299px;font-size:27px}
.front-phonebar{left:470px;top:343px;width:305px;height:43px;background:var(--yellow);border-radius:22px 0 0 22px}
.phone-line{display:flex;align-items:center;gap:8px;font:700 23px/1 'Lato',sans-serif;color:var(--ink);white-space:nowrap}
.phone-line b{color:var(--red);font-weight:900}
.front-phone{left:494px;top:352px}

/* back */
.back-header{left:0;top:0;width:612px;height:141px;background:var(--ink)}
.back-seal{left:16px;top:7px;width:152px;height:152px;border-radius:50%;background:var(--white);border:5px solid var(--ink);display:flex;align-items:center;justify-content:center;text-align:center}
.back-seal span{font:900 21px/24px 'Montserrat',sans-serif;color:var(--ink)}
.back-title{left:190px;top:36px;width:405px;text-align:center;font:900 40px/48px 'Montserrat',sans-serif;color:var(--yellow);white-space:nowrap}
.back-subtitle{left:202px;top:87px;width:385px;display:flex;align-items:center;gap:12px;font:700 27px/30px 'Lato',sans-serif;color:var(--yellow);letter-spacing:1px}
.back-subtitle::before,.back-subtitle::after{content:"";flex:1;height:2px;background:var(--white)}
.postage{left:624px;top:22px;width:127px;height:125px;border:1px solid var(--grey-line);font:700 11px/125px Arial,sans-serif;text-align:center;color:var(--ink)}
.guarantee{left:156px;top:143px;width:268px;height:24px;font:900 15.5px/24px 'Lato',sans-serif;color:var(--ink);text-align:center;white-space:nowrap}
.guarantee i{color:var(--red);font-style:normal}
.info-panel{left:0;top:169px;width:420px;height:250px;background:var(--yellow)}
.pitch{left:16px;top:180px;font:400 16.5px/20px 'Lato',sans-serif;color:var(--ink)}
.pitch strong{font-weight:700;font-style:italic}
.back-phonepill{left:16px;top:251px;width:317px;height:34px;background:var(--ink);border-radius:17px}
.back-phone{left:26px;top:256px;color:var(--white)}
.back-phone svg circle{fill:var(--yellow)}
.contact-list{left:37px;top:291px;list-style:none;font:400 17px/19.5px 'Lato',sans-serif;color:var(--ink)}
.contact-list li{display:flex;align-items:center;gap:6px}
.owner-photo{left:0;top:364px;width:157px;height:159px;background:linear-gradient(180deg,#d8dde2,#1f2d48);clip-path:polygon(0 0,55% 0,100% 22%,100% 100%,0 100%)}
.back-signature{left:150px;top:368px;font-size:24px;color:var(--ink)}
.owner-role{left:150px;top:396px;font:700 14.5px/16px 'Lato',sans-serif;color:var(--ink);white-space:nowrap}
.vet-badge{left:314px;top:322px;width:88px;height:88px;border-radius:50%;background:var(--white);border:6px solid #1b3f8f}
.address{left:474px;top:298px;font:400 17px/24.5px Arial,sans-serif;color:var(--ink);font-style:normal}
</style>
</head>
<body>

<section class="card card-front">
  <div class="photo-row top">
    <div class="photo ph-assembly" role="img" aria-label="Furniture parts and tools laid out for assembly"></div>
    <div class="photo ph-router" role="img" aria-label="Wireless router with glowing signal rings"></div>
    <div class="photo ph-plumbing" role="img" aria-label="Hands fitting a white drain pipe"></div>
    <div class="photo ph-siding" role="img" aria-label="Outdoor fixture mounted on house siding"></div>
  </div>
  <div class="abs front-topline"></div>
  <div class="abs front-tagstrip"></div>
  <p class="abs tagline">DON'T FEEL LIKE DOING IT<br>OR JUST DON'T HAVE TIME?</p>
  <div class="abs services-pill">SERVICES</div>
  <ul class="abs services-list">
    <li>Assembly</li><li>Small Repairs</li><li>Wifi / Router Setup</li><li>Fabrication</li><li>Hanging Items</li><li>Wireless Device Setup</li><li>Odd Jobs</li>
  </ul>
  <div class="abs brand-seal"><span>BRISK<br>FIXERS 24</span></div>
  <h2 class="abs headline">Get it Done <em>NOW!</em></h2>
  <div class="abs headline-rule"></div>
  <ul class="abs benefits">
    <li>FAST RESPONSE</li><li>HIGH QUALITY</li><li>FAIR PRICING</li><li>VETERAN OWNED</li>
  </ul>
  <p class="abs signature front-signature">Dana R Holcomb</p>
  <div class="abs front-phonebar"></div>
  <div class="abs phone-line front-phone">
    <svg width="24" height="24" viewBox="0 0 24 24"><circle cx="12" cy="12" r="12" fill="#171c24"/><path d="M8.5 6.5l2 2-1.2 1.6a7 7 0 0 0 4.6 4.6l1.6-1.2 2 2-1.5 1.8c-4.8 0-9.3-4.5-9.3-9.3z" fill="#fde400"/></svg>
    (555) 304-7182 <b>TEXT</b>
  </div>
  <div class="abs front-bottomline"></div>
  <div class="photo-row bottom">
    <div class="photo ph-doorbell" role="img" aria-label="Video doorbell installed beside a stone wall"></div>
    <div class="photo ph-tvmount" role="img" aria-label="TV wall mount bracket with tools"></div>
    <div class="photo ph-curtain" role="img" aria-label="Curtains hung on a rod by a window"></div>
    <div class="photo ph-paint" role="img" aria-label="Hand painting colourful strokes on a wall"></div>
  </div>
</section>

<section class="card card-back">
  <div class="abs back-header"></div>
  <div class="abs back-seal"><span>BRISK<br>FIXERS 24</span></div>
  <h1 class="abs back-title">BRISK FIXERS 24</h1>
  <div class="abs back-subtitle">HANDYMAN</div>
  <div class="abs postage">POSTAGE</div>
  <p class="abs guarantee"><i>&#9733;</i>SATISFACTION GUARANTEED<i>&#9733;</i></p>
  <div class="abs info-panel"></div>
  <p class="abs pitch">I want what I want when I want it and<br>I want it done right. You deserve the same.<br><strong>Send a text and I will respond immediately.</strong></p>
  <div class="abs back-phonepill"></div>
  <div class="abs phone-line back-phone">
    <svg width="24" height="24" viewBox="0 0 24 24"><circle cx="12" cy="12" r="12"/><path d="M8.5 6.5l2 2-1.2 1.6a7 7 0 0 0 4.6 4.6l1.6-1.2 2 2-1.5 1.8c-4.8 0-9.3-4.5-9.3-9.3z" fill="#171c24"/></svg>
    (555) 304-7182 <b>TEXT</b>
  </div>
  <ul class="abs contact-list">
    <li><svg width="13" height="15" viewBox="0 0 12 16"><path d="M6 0a6 6 0 0 0-6 6c0 4.5 6 10 6 10s6-5.5 6-10a6 6 0 0 0-6-6zm0 8.5A2.5 2.5 0 1 1 6 3.5a2.5 2.5 0 0 1 0 5z" fill="#171c24"/></svg>Harbor Point, Florida</li>
    <li><svg width="14" height="11" viewBox="0 0 14 11"><rect width="14" height="11" fill="#171c24"/><path d="M0 0l7 6 7-6" stroke="#fde400" fill="none"/></svg>Service@BriskFixers24.com</li>
    <li><svg width="14" height="14" viewBox="0 0 14 14"><circle cx="7" cy="7" r="6.3" fill="none" stroke="#171c24" stroke-width="1.4"/><path d="M1 7h12M7 1c-3 3-3 9 0 12M7 1c3 3 3 9 0 12" stroke="#171c24" fill="none" stroke-width="1.1"/></svg>BriskFixers24.com</li>
  </ul>
  <div class="abs owner-photo" role="img" aria-label="Portrait photo of the owner in a suit"></div>
  <p class="abs signature back-signature">Dana R Holcomb</p>
  <p class="abs owner-role">OWNER &amp; HANDYMAN</p>
  <div class="abs vet-badge"></div>
  <address class="abs address">John Smith<br>123 Main Street<br>Small Town, USA 00000-0000</address>
</section>

</body>
</html>
```